a small documentary making company needs a fancy simple website

Hi

Need a Website that is classic and funky at the same time

I have a simple design already made up but need some advice and someone to give it that wow factor.

the structure should be simple, my proposition is:

Home Page:
* Home
* Store
** Purchase (Trailer Preview / Desc / Info)
** (Purchase options: Buy DVD / Rent/View 48 Hrs)
* Portfolio
** Who we are
** Projects
** Media Presence
* Contact

I have the logo and proposed design, our launch date is 13/05/2012 so we need this site developed / up and running in two weeks.

this job is for a design + code

Faithfully
Leopold

Target Market(s)

Spiritual and Religious

Industry/Entity Type

It Company

Requirements
Must have
• * Ability to sell dvd's
* Google & Bing search friendly
* Play video Trailers
Nice to have
• Flash Interface

```html
<!DOCTYPE html>
<html lang="en">
<head>
<meta charset="utf-8">
<title>Vesper Hall Films</title>
<link rel="stylesheet" href="https://fonts.googleapis.com/css2?family=Cinzel:wght@400;500&display=swap">
<style>
  :root {
    --page-bg: #171717;
    --header-top: #1b1b1b;
    --header-bottom: #0c0c0c;
    --nav-band: rgba(8, 8, 8, 0.62);
    --nav-active: #050505;
    --menu-bg: #030303;
    --cart-bg: rgba(0, 0, 0, 0.72);
    --quote-bg: rgba(10, 10, 10, 0.62);
    --text: #f4f1ea;
    --stone-dark: #2b2218;
    --stone-mid: #6a5436;
    --stone-warm: #a8865a;
    --light: #f3e2b8;
  }
  * { margin: 0; padding: 0; box-sizing: border-box; }
  html, body { width: 1200px; height: 800px; overflow: hidden; }
  body {
    background: var(--page-bg);
    font-family: "Cinzel", "Times New Roman", serif;
    color: var(--text);
    position: relative;
  }
  .site-header {
    position: absolute; left: 0; top: 0; width: 1200px; height: 120px;
    background: linear-gradient(to bottom, var(--header-top), var(--header-bottom));
  }
  .brand {
    position: absolute; left: 0; top: 28px; width: 1200px;
    display: flex; justify-content: center; align-items: center; gap: 14px;
    font-size: 38px; font-weight: 400; letter-spacing: 1px; color: var(--text);
    text-decoration: none;
  }
  .brand-mark {
    width: 34px; height: 34px; border-radius: 50%;
    border: 2px solid var(--text);
  }
  .hero {
    position: absolute; left: 0; top: 120px; width: 1200px; height: 480px;
    background:
      radial-gradient(ellipse 160px 220px at 720px 190px, rgba(243, 226, 184, 0.85), rgba(243, 226, 184, 0) 70%),
      radial-gradient(ellipse 90px 120px at 95px 280px, rgba(190, 150, 90, 0.7), rgba(190, 150, 90, 0) 75%),
      radial-gradient(ellipse 700px 160px at 800px 430px, rgba(200, 170, 120, 0.55), rgba(200, 170, 120, 0) 70%),
      linear-gradient(to bottom, var(--stone-dark) 0%, var(--stone-mid) 45%, var(--stone-warm) 72%, #5a4a36 100%);
  }
  .main-nav {
    position: absolute; left: 0; top: 120px; width: 1200px; height: 40px;
    background: var(--nav-band);
  }
  .nav-list { list-style: none; position: absolute; left: 408px; top: 0; display: flex; }
  .nav-item { position: relative; }
  .nav-item > a {
    display: block; height: 40px; line-height: 42px; padding: 0 20px;
    color: var(--text); text-decoration: none; font-size: 13px; letter-spacing: 0.5px;
  }
  .nav-item.is-open > a { background: var(--nav-active); }
  .submenu {
    list-style: none; position: absolute; left: 0; top: 40px;
    width: 211px; height: 84px; background: var(--menu-bg);
    padding: 17px 0 0 15px;
  }
  .submenu a {
    display: block; color: var(--text); text-decoration: none;
    font-size: 13px; line-height: 18px; letter-spacing: 0.3px;
  }
  .cart {
    position: absolute; left: 980px; top: 0; width: 120px; height: 40px;
    background: var(--cart-bg); padding-left: 11px;
    line-height: 42px; font-size: 12px; color: var(--text); text-decoration: none;
  }
  .tagline {
    position: absolute; left: 0; top: 468px; width: 601px; height: 90px;
    background: var(--quote-bg); padding: 12px 0 0 118px;
    font-size: 20px; line-height: 19px; font-weight: 500; letter-spacing: 0.3px;
  }
  .tagline::first-letter { font-size: 30px; }
  .site-footer {
    position: absolute; left: 0; top: 616px; width: 1200px; text-align: center;
    font-size: 10.5px; line-height: 18px; letter-spacing: 0.2px;
  }
  .site-footer a { color: var(--text); text-decoration: none; }
</style>
</head>
<body>
  <header class="site-header">
    <a class="brand" href="#"><span class="brand-mark"></span>Vesper Hall Films</a>
  </header>

  <div class="hero" role="img" aria-label="Photograph of a sunlit gothic cloister with stone arches and a worn tiled floor"></div>

  <nav class="main-nav">
    <ul class="nav-list">
      <li class="nav-item"><a href="#">Home</a></li>
      <li class="nav-item"><a href="#">Store</a></li>
      <li class="nav-item is-open"><a href="#">Portfolio</a>
        <ul class="submenu">
          <li><a href="#">Who we are</a></li>
          <li><a href="#">Projects</a></li>
          <li><a href="#">Media presence</a></li>
        </ul>
      </li>
      <li class="nav-item"><a href="#">Contact</a></li>
    </ul>
    <a class="cart" href="#">Cart : 0</a>
  </nav>

  <p class="tagline">In the end, it's not going to matter how many breaths you took, but how many moments took your breath away.</p>

  <footer class="site-footer">
    <p>Copyright © 2012 Vesper Hall Films. Use of this website constitutes acceptance of our <a href="#">User Agreement</a></p>
    <p><a href="#">Privacy Policy</a></p>
  </footer>
</body>
</html>
```